Admin Backend Redesign

We need a redesign for our backend which supoosed to make the backoffice look more modern!

I will add screenshots of the backoffice so you know what data will be shown in the Admin.

Have in mind that the users of this backend are Doctors. We need a clinical look, modern and sharp. The backoffice is responsive, have that in mind. We need the backoffice to look as professional as possible.

The theme used for the website is: http://velmora.brisk-sample.net/

ON the main page of the backoffice, under every widget i need some space to write an explanation what the widget is about.

The color code used in our logo and website is #57aad4 combined with white.

We are open for ideas!
Updates

Project Deadline Extended
Reason: Designs are ok, but nothing innovative. Please use more modern designs!

Project Deadline Extended
Reason: Havent recieved a perfect design yet. Please read instructions carefully! Thank you

Project Deadline Extended
Reason: Hey everybody, sorry for the delay. We will decide in 3 days. If anyone wants to add a Design, that would be great.

Target Market(s)

Doctors, therapists

Industry/Entity Type

It Professional

Font styles to use
Sans Serif

Requirements
Must have
• Must look uptodate, modern, like new back offices look nowadays

```html
<!DOCTYPE html>
<html lang="de">
<head>
<meta charset="utf-8">
<title>Admin Dashboard</title>
<link rel="stylesheet" href="https://fonts.googleapis.com/css2?family=Open+Sans:ital,wght@0,400;0,600;0,700;1,400&display=swap">
<style>
:root{
  --brand:#57aad4;
  --brand-soft:#b3d6ea;
  --page:#e8edf1;
  --white:#ffffff;
  --ink:#222222;
  --muted:#9a9a9a;
  --line:#e4e4e4;
  --green:#3cc04a;
  --chart-fill:#b2dbb4;
  --chart-line:#4fc35a;
  --plot-bg:#ececec;
  --orange:#fbac4d;
  --teal:#15a8a4;
  --red:#e84a64;
  --sky:#4cc0f2;
  --slate:#4d7882;
  --mint:#4fd8c1;
  --pink:#f98a8a;
  --alert:#e74c3c;
}
*{box-sizing:border-box;margin:0;padding:0}
html,body{width:1200px;height:1199px;overflow:hidden}
body{font-family:"Open Sans",Arial,sans-serif;background:var(--page);color:var(--ink);position:relative}
.topbar{position:absolute;left:0;top:0;width:1200px;height:53px;background:var(--white);}
.topbar .menu-toggle{position:absolute;left:34px;top:21px}
.topbar .brand-name{position:absolute;left:0;right:0;top:14px;text-align:center;font-size:17px}
.topbar .tools{position:absolute;right:30px;top:12px;display:flex;align-items:center;gap:14px}
.bell{position:relative}
.bell .count{position:absolute;right:-3px;top:-2px;width:8px;height:8px;border-radius:50%;background:var(--alert)}
.avatar{width:31px;height:31px;border-radius:50%;border:2px solid var(--brand);background:linear-gradient(#dfe8ee,#9fb6c4)}
.sidebar{position:absolute;left:0;top:53px;width:246px;height:1146px;background:var(--brand)}
.nav-item{position:absolute;left:32px;display:flex;align-items:center;gap:18px;color:var(--white);font-size:13px;white-space:nowrap}
.nav-item.active::after{content:"";position:absolute;left:204px;top:3px;border:10px solid transparent;border-right-color:var(--page);border-left:0}
.card{position:absolute;background:var(--white);border-radius:3px;overflow:hidden}
.card-head{height:36px;background:var(--brand);color:var(--ink);font-size:16px;padding:6px 17px;display:flex;justify-content:space-between;align-items:center}
.card-head b{font-weight:700}
.list-icon{width:14px;height:10px}
.note{position:absolute;left:17px;bottom:16px;font-size:9.5px;font-style:italic;white-space:nowrap}
.left{left:282px;width:433px}
.right{left:733px;width:432px}
.hero .art{position:absolute;left:22px;top:8px;width:100px;height:114px;border-radius:40px 40px 6px 6px;background:linear-gradient(#c9d3dc,#7d8fa0)}
.hero .strip{position:absolute;left:0;bottom:0;width:100%;height:23px;background:var(--brand-soft);font-size:12px;text-align:right;padding:3px 12px;display:flex;justify-content:flex-end;align-items:center;gap:6px}
.hero h2{position:absolute;left:164px;top:30px;font-size:33px;font-weight:400;line-height:1;white-space:nowrap}
.hero p{position:absolute;left:164px;top:67px;font-size:16px;white-space:nowrap}
.welcome-text{padding:14px 17px;font-size:12.2px;line-height:1.37;text-align:justify}
.btn-ok{display:inline-block;margin-top:9px;background:var(--green);color:var(--white);font-weight:700;font-size:12px;padding:5px 15px;border-radius:3px}
.legend{position:absolute;font-size:12px;width:90px;height:44px}
.legend .bar{position:absolute;left:0;top:0;width:7px;height:44px}
.legend .name{position:absolute;left:19px;top:0;white-space:nowrap;line-height:16px}
.legend .value{position:absolute;left:19px;top:19px;font-size:20px;line-height:26px;white-space:nowrap}
.note-row{height:42px;border-bottom:1px solid var(--line);display:flex;justify-content:space-between;align-items:center;padding:0 19px 0 18px;font-size:12.5px;white-space:nowrap}
.tag{width:61px;height:15px;background:var(--green);color:var(--white);font-size:10px;font-weight:700;text-align:center;line-height:15px;border-radius:2px}
.cal-title{position:absolute;top:46px;left:0;width:100%;text-align:center;font-size:16px}
.cal-grid{position:absolute;left:28px;top:80px;width:376px;display:grid;grid-template-columns:repeat(7,1fr);row-gap:9px;font-size:13px;color:var(--muted);text-align:center}
.cal-grid .dow{color:#555;font-weight:600;margin-bottom:9px}
.cal-grid .today{color:var(--white);background:var(--green);font-weight:700;width:28px;height:28px;line-height:28px;margin:-6px auto;}
.cal-grid .faint{color:#ccc}
</style>
</head>
<body>
<header class="topbar">
  <svg class="menu-toggle" width="13" height="10" viewBox="0 0 13 10"><path d="M0 1h13M0 5h13M0 9h13" stroke="#57aad4" stroke-width="1.3"/></svg>
  <div class="brand-name">Logo goes here</div>
  <div class="tools">
    <span class="bell"><svg width="16" height="17" viewBox="0 0 16 17" fill="none" stroke="#57aad4" stroke-width="1.4"><path d="M3 12V7a5 5 0 0 1 10 0v5l1.5 2h-13z"/><path d="M6.5 15.5a1.5 1.5 0 0 0 3 0"/></svg><span class="count"></span></span>
    <svg width="16" height="16" viewBox="0 0 16 16" fill="none" stroke="#57aad4" stroke-width="1.4"><circle cx="8" cy="8" r="2.5"/><path d="M8 1v2.5M8 12.5V15M1 8h2.5M12.5 8H15M3 3l1.8 1.8M11.2 11.2L13 13M3 13l1.8-1.8M11.2 4.8L13 3"/></svg>
    <div class="avatar" role="img" aria-label="Profile photo of the signed-in doctor"></div>
  </div>
</header>

<nav class="sidebar">
  <div class="nav-item active" style="top:52px"><svg width="22" height="22" viewBox="0 0 22 22" fill="none" stroke="#fff" stroke-width="1.4"><path d="M2 11L11 2l9 9M5 8v12h12V8"/></svg>Dashboard</div>
  <div class="nav-item" style="top:99px"><svg width="22" height="22" viewBox="0 0 22 22" fill="none" stroke="#fff" stroke-width="1.4"><circle cx="11" cy="7" r="5"/><path d="M2 21c0-5 4-8 9-8s9 3 9 8z"/></svg>Mein Konto</div>
  <div class="nav-item" style="top:146px"><svg width="22" height="22" viewBox="0 0 22 22" fill="none" stroke="#fff" stroke-width="1.4"><path d="M17 11v9H2V5h9"/><path d="M18 2l3 3-9 9H9v-3z"/></svg>Patientenbewertungen</div>
</nav>

<section class="card hero left" style="top:71px;height:122px">
  <div class="art" role="img" aria-label="Illustration of a doctor in a white coat with stethoscope"></div>
  <h2>Profil</h2><p>Profil bearbeiten</p>
  <div class="strip">Weiter <svg width="14" height="14" viewBox="0 0 14 14" fill="none" stroke="#222" stroke-width="1.2"><circle cx="7" cy="7" r="6"/><path d="M4 7h6M7.5 4.5L10 7l-2.5 2.5"/></svg></div>
</section>
<section class="card hero right" style="top:71px;height:122px">
  <div class="art" role="img" aria-label="Illustration of a bandaged patient in a hospital gown" style="background:linear-gradient(#d8c9b0,#6fa3c9)"></div>
  <h2>Patienten</h2><p>Patienten verwalten</p>
  <div class="strip">Alle Ansehen <svg width="14" height="14" viewBox="0 0 14 14" fill="none" stroke="#222" stroke-width="1.2"><circle cx="7" cy="7" r="6"/><path d="M4 7h6M7.5 4.5L10 7l-2.5 2.5"/></svg></div>
</section>

<section class="card left" style="top:211px;height:210px">
  <div class="card-head"><span>Willkommen: <b>Dr. Mustermann</b></span><svg class="list-icon" viewBox="0 0 14 10"><path d="M0 1h2M4 1h10M0 5h2M4 5h10M0 9h2M4 9h10" stroke="#222" stroke-width="1.3"/></svg></div>
  <div class="welcome-text">Proin gravida nibh vel velit auctor aliquet. Aenean sollicitudin, lorem quis bibendum auctor, nisi elit consequat ipsum, nec sagittis sem nibh id elit. Duis sed odio sit amet nibh vulputate cursus a sit amet mauris. Morbi accumsan ipsum velit. Nam nec tellus a odio tincidunt auctor a ornare odio. Sed non &nbsp;mauris vitae erat consequat auctor eu in elit. Duis sed odio sit amet nibh.<br><span class="btn-ok">Alles OK</span></div>
</section>

<section class="card right" style="top:211px;height:263px">
  <div class="card-head"><span>Trend Graph &amp; Chart</span><svg class="list-icon" viewBox="0 0 14 10"><path d="M0 1h2M4 1h10M0 5h2M4 5h10M0 9h2M4 9h10" stroke="#222" stroke-width="1.3"/></svg></div>
  <svg style="position:absolute;left:0;top:0" width="432" height="240" viewBox="0 0 432 240" font-family="Open Sans, sans-serif" font-size="10.5" fill="#222">
    <rect x="62" y="55" width="316" height="129" fill="#ececec" stroke="#bbb" stroke-width=".7"/>
    <path d="M62 98.5H378M62 141.5H378" stroke="#c8c8c8" stroke-width=".7"/>
    <path d="M62 141L122 184L188 158L252 98L314 115L377 104V184H62Z" fill="#b2dbb4"/>
    <polyline points="62,141 122,184 188,158 252,98 314,115 377,104" fill="none" stroke="#4fc35a" stroke-width="1.5"/>
    <g fill="#4fc35a"><circle cx="62" cy="141" r="3"/><circle cx="122" cy="184" r="3"/><circle cx="188" cy="158" r="3"/><circle cx="252" cy="98" r="3"/><circle cx="314" cy="115" r="3"/><circle cx="377" cy="104" r="3"/></g>
    <g text-anchor="end"><text x="43" y="59">15</text><text x="43" y="102">10</text><text x="43" y="145">5</text><text x="43" y="188">0</text></g>
    <g text-anchor="middle"><text x="62" y="213">Oct 2012</text><text x="122" y="213">Jan 2013</text><text x="188" y="213">Apr 2013</text><text x="252" y="213">Oct 2013</text><text x="314" y="213">Jan 2014</text><text x="377" y="213">Apr 2014</text></g>
  </svg>
  <div class="note">* This widget is used for lorem quis bibendum auctor, nisi elit consequat ipsum.</div>
</section>

<section class="card left" style="top:492px;height:264px">
  <div class="card-head"><span>Pie Chart</span><svg class="list-icon" viewBox="0 0 14 10"><path d="M0 1h2M4 1h10M0 5h2M4 5h10M0 9h2M4 9h10" stroke="#222" stroke-width="1.3"/></svg></div>
  <svg style="position:absolute;left:55px;top:58px" width="166" height="166" viewBox="0 0 166 166">
    <g transform="rotate(-90 83 83)" fill="none" stroke-width="26">
      <circle cx="83" cy="83" r="66" pathLength="100" stroke="#e84a64" stroke-dasharray="20 80"/>
      <circle cx="83" cy="83" r="66" pathLength="100" stroke="#15a8a4" stroke-dasharray="0 20 47 33"/>
      <circle cx="83" cy="83" r="66" pathLength="100" stroke="#4cc0f2" stroke-dasharray="0 67 26 7"/>
      <circle cx="83" cy="83" r="66" pathLength="100" stroke="#fbac4d" stroke-dasharray="0 93 7 0"/>
    </g>
    <text x="83" y="80" text-anchor="middle" font-family="Open Sans, sans-serif" font-size="20">JUNE</text>
    <text x="83" y="104" text-anchor="middle" font-family="Open Sans, sans-serif" font-size="20">2013</text>
  </svg>
  <div class="legend" style="left:235px;top:85px"><span class="bar" style="background:var(--orange)"></span><span class="name">Cancer</span><span class="value">9%</span></div>
  <div class="legend" style="left:333px;top:85px"><span class="bar" style="background:var(--teal)"></span><span class="name">TBC</span><span class="value">48%</span></div>
  <div class="legend" style="left:235px;top:146px"><span class="bar" style="background:var(--red)"></span><span class="name">Bird Flu</span><span class="value">21%</span></div>
  <div class="legend" style="left:333px;top:146px"><span class="bar" style="background:var(--sky)"></span><span class="name">Asthma</span><span class="value">32%</span></div>
  <div class="note">* This widget is used for lorem quis bibendum auctor, nisi elit consequat ipsum.</div>
</section>

<section class="card right" style="top:492px;height:264px">
  <div class="card-head"><span>Pie Chart</span><svg class="list-icon" viewBox="0 0 14 10"><path d="M0 1h2M4 1h10M0 5h2M4 5h10M0 9h2M4 9h10" stroke="#222" stroke-width="1.3"/></svg></div>
  <svg style="position:absolute;left:0;top:36px" width="432" height="190" viewBox="0 0 432 190" font-family="Open Sans, sans-serif">
    <g transform="rotate(-90 216 97)" fill="none" stroke-width="12">
      <circle cx="216" cy="97" r="75" pathLength="100" stroke="#4d7882" stroke-dasharray="58 42"/>
      <circle cx="216" cy="97" r="75" pathLength="100" stroke="#4fd8c1" stroke-dasharray="0 58 23 19"/>
      <circle cx="216" cy="97" r="75" pathLength="100" stroke="#f98a8a" stroke-dasharray="0 81 19 0"/>
    </g>
    <path d="M285 119L337 133" stroke="#4d7882" stroke-width="1.3"/><circle cx="337" cy="133" r="2.5" fill="#4d7882"/>
    <path d="M146 121L89 134" stroke="#4fd8c1" stroke-width="1.3"/><circle cx="89" cy="134" r="2.5" fill="#4fd8c1"/>
    <path d="M161 43L140 25" stroke="#f98a8a" stroke-width="1.3"/><circle cx="140" cy="25" r="2.5" fill="#f98a8a"/>
    <text x="343" y="138" font-size="15" fill="#4d7882">57%</text>
    <text x="46" y="140" font-size="15" fill="#4fd8c1">30%</text>
    <text x="97" y="32" font-size="15" fill="#f98a8a">23%</text>
    <g text-anchor="middle" font-size="19"><text x="216" y="73" fill="#4d7882">Adults</text><text x="216" y="101" fill="#4fd8c1">Elders</text><text x="216" y="129" fill="#f98a8a">Kids</text></g>
  </svg>
  <div class="note">* This widget is used for lorem quis bibendum auctor, nisi elit consequat ipsum.</div>
</section>

<section class="card left" style="top:774px;height:264px">
  <div class="card-head"><span>Notes</span><svg class="list-icon" viewBox="0 0 14 10"><path d="M0 1h2M4 1h10M0 5h2M4 5h10M0 9h2M4 9h10" stroke="#222" stroke-width="1.3"/></svg></div>
  <div class="note-row"><span>Once upon a time i was a doctor.</span><span class="tag">Personal</span></div>
  <div class="note-row"><span>Making a sandwich on Saturday.</span><span class="tag">Work</span></div>
  <div class="note-row"><span>Make pasta from John’s recipe.</span><span class="tag">Food</span></div>
  <div class="note-row"><span>Meeting on Tuesday with Dr. Gwen.</span><span class="tag">Office</span></div>
  <div class="note">* This widget is used for lorem quis bibendum auctor, nisi elit consequat ipsum.</div>
</section>

<section class="card right" style="top:774px;height:264px">
  <div class="card-head"><span>Calender</span><svg class="list-icon" viewBox="0 0 14 10"><path d="M0 1h2M4 1h10M0 5h2M4 5h10M0 9h2M4 9h10" stroke="#222" stroke-width="1.3"/></svg></div>
  <div class="cal-title"><svg width="8" height="11" viewBox="0 0 8 11" style="margin-right:38px"><path d="M6 1L2 5.5 6 10" fill="none" stroke="#222" stroke-width="2"/></svg>June 2013<svg width="8" height="11" viewBox="0 0 8 11" style="margin-left:38px"><path d="M2 1l4 4.5L2 10" fill="none" stroke="#222" stroke-width="2"/></svg></div>
  <div class="cal-grid">
    <span class="dow">S</span><span class="dow">M</span><span class="dow">T</span><span class="dow">W</span><span class="dow">R</span><span class="dow">F</span><span class="dow">S</span>
    <span></span><span>1</span><span>2</span><span>3</span><span>4</span><span>5</span><span>6</span>
    <span>7</span><span>8</span><span>9</span><span>10</span><span>11</span><span class="faint">12</span><span>13</span>
    <span>14</span><span>15</span><span>16</span><span>17</span><span>18</span><span>19</span><span>20</span>
    <span>21</span><span>22</span><span>23</span><span class="today">24</span><span>25</span><span>26</span><span>27</span>
    <span>28</span><span>29</span><span>30</span><span>31</span><span></span><span></span><span></span>
  </div>
</section>
</body>
</html>
```